Data/Computer Security company needs a brochure design

We need a brochure design for Vaultmere Lens.
We deliver security solutions that manage critical risks, protect vital information and provide regulatory compliance. (mostly professional offices and small businesses with an emphasis in financial services) Optimal security is achieved through agent-based auditing and network activity monitoring.
Specialists in the area of helping Broker/Dealers and Independent Financial Service Representatives measure field office security, threat readiness and compliance with current policies and procedures. We provide auditors with clear, concise reports of policy deviations along with guidance in closing gaps, weaknesses or deficiencies.
Our services allow audit staff efficiency and productivity in their process while ensuring the field offices are utilizing best security practices and exercising the appropriate level of diligence and care in protecting the client information entrusted to them.
More about process and services can be seen on our website - www.vaultmerelens.example
We use blues and grays in our designs.
Financial

```html
<!DOCTYPE html>
<html lang="en">
<head>
<meta charset="utf-8">
<title>Vaultmere Lens – Pricing</title>
<link rel="stylesheet" href="https://fonts.googleapis.com/css2?family=Open+Sans:wght@400;600;700&display=swap">
<style>
  :root {
    --stage: #3a3a3c;
    --panel-deep: #031019;
    --panel-dark: #062a3d;
    --panel-mid: #0b5470;
    --panel-bright: #2ba3c6;
    --panel-glow: #7ddcf2;
    --text-main: #ffffff;
    --text-soft: #d7eef6;
    --contact-fill: rgba(150, 200, 220, 0.24);
    --contact-edge: rgba(190, 230, 245, 0.35);
  }
  * { box-sizing: border-box; margin: 0; padding: 0; }
  html, body {
    width: 1200px; height: 793px; overflow: hidden;
    background: var(--stage);
    font-family: "Open Sans", Arial, sans-serif;
  }
  .canvas { position: relative; width: 1200px; height: 793px; }
  .pricing-panel {
    position: absolute; left: 300px; top: 96px;
    width: 610px; height: 600px; overflow: hidden;
    background: var(--panel-deep);
    color: var(--text-main);
  }
  .panel-art {
    position: absolute; inset: 0;
    background:
      radial-gradient(ellipse 14% 42% at 47% 10%, rgba(125,220,242,0.75), transparent 70%),
      radial-gradient(ellipse 22% 9% at 44% 45%, rgba(125,220,242,0.55), transparent 75%),
      radial-gradient(ellipse 38% 20% at 25% 78%, rgba(43,163,198,0.85), transparent 75%),
      radial-gradient(ellipse 45% 30% at 20% 20%, rgba(43,163,198,0.55), transparent 75%),
      radial-gradient(ellipse 30% 18% at 30% 52%, rgba(3,16,25,0.75), transparent 75%),
      linear-gradient(135deg, var(--panel-mid) 0%, var(--panel-bright) 30%, var(--panel-dark) 55%, var(--panel-mid) 68%, var(--panel-deep) 100%);
  }
  .panel-title {
    position: absolute; left: 352px; top: 18px;
    font-size: 46px; font-weight: 700; letter-spacing: 0.5px;
  }
  .price-copy {
    position: absolute; left: 357px; top: 100px; width: 230px;
    font-size: 10.5px; line-height: 1.4; color: var(--text-main);
  }
  .price-copy strong { font-weight: 700; }
  .price-amount { font-size: 28px; font-weight: 400; line-height: 1; vertical-align: -3px; }
  .price-copy p + p { margin-top: 12px; }
  .contact-box {
    position: absolute; left: 368px; top: 446px;
    width: 210px; height: 110px; padding: 8px 12px;
    border-radius: 9px;
    background: var(--contact-fill);
    border: 1px solid var(--contact-edge);
    color: var(--text-soft);
  }
  .contact-heading { font-size: 13px; font-weight: 400; color: var(--text-main); line-height: 1.2; margin-bottom: 3px; }
  .contact-line { font-size: 8px; line-height: 1.35; }
  .brand {
    position: absolute; left: 58px; top: 494px;
    display: flex; align-items: center; gap: 10px;
  }
  .brand-mark { width: 14px; height: 14px; border-radius: 50%; background: var(--text-main); flex: none; }
  .brand-name { font-size: 22px; font-weight: 700; line-height: 1.05; color: var(--text-main); }
</style>
</head>
<body>
<main class="canvas">
  <section class="pricing-panel">
    <div class="panel-art" role="img" aria-label="Abstract blue digital globe with wireframe grid and streaks of light"></div>

    <h1 class="panel-title">PRICING</h1>

    <div class="price-copy">
      <p><strong>Monthly fee of </strong><span class="price-amount">$13.50</span><strong> per computer.</strong> Sales tax may be applicable in some areas.</p>
      <p>With Vaultmere Lens’s unique services, the security of personal and confidential information does not need to be burdensome, intrusive or expensive.</p>
    </div>

    <div class="contact-box">
      <h2 class="contact-heading">CONTACT US</h2>
      <p class="contact-line">Vaultmere Lens LLC</p>
      <p class="contact-line">4870 Harborview Lane, Ste. B-12</p>
      <p class="contact-line">Marlow, IA 50990</p>
      <p class="contact-line">US</p>
      <p class="contact-line">Phone: (555) 014-2290</p>
      <p class="contact-line">Email: info@vaultmerelens.example</p>
    </div>

    <div class="brand">
      <span class="brand-mark"></span>
      <span class="brand-name">Vaultmere<br>Lens</span>
    </div>
  </section>
</main>
</body>
</html>
```